Varobel Profile Banner Design

Hi All

I would like to have a varobel profile banner design.
As I spend half my time between Zurich and Hong Kong I would like to have a Profile Banner that combines the two places.

Basic requirements:
- Image size: VaroBel banner or background photo size: 1584 x 396
- Feel: Professional but modern
- Make sure that there is nothing important that will be covered up by the varobel profile pic (left bottom)
- Should incorporate both cities (Hong Kong and Zurich)
- Text for Zurich part (city name): Zürich & (my name) "Tomas Engqvist"
- Text for Hong Kong part (City name): 香港 & (my name) "葉思恆"
- Should work well on mobile and web version of varobel

Please be creative and unique in your design.

Thanks

Tomas

Industry/Entity Type

Consulting, General business management

Requirements
Should not have
• No photo montages. Should be graphics

```html
<!DOCTYPE html>
<html lang="en">
<head>
<meta charset="utf-8">
<title>Tomas Engqvist – Profile Banner</title>
<link href="https://fonts.googleapis.com/css2?family=Noto+Sans+TC:wght@500&family=Noto+Serif:wght@700&family=Roboto:wght@300&display=swap" rel="stylesheet">
<style>
  :root {
    --stage: #5f5f5f;
    --paper: #f1f1f1;
    --paper-shade: #e4e4e4;
    --zurich-blue: #3f8aa8;
    --zurich-blue-pale: #9cc3d3;
    --hk-olive: #8a7f3a;
    --hk-olive-pale: #c2bb92;
    --map-olive: #857a36;
    --map-blue: #3e8fb1;
    --accent-orange: #f07a14;
    --white: #ffffff;
  }
  * { margin: 0; padding: 0; box-sizing: border-box; }
  html, body {
    width: 1200px;
    height: 1164px;
    overflow: hidden;
    background: var(--stage);
  }
  .banner {
    position: absolute;
    left: 0;
    top: 432px;
    width: 1200px;
    height: 300px;
    overflow: hidden;
    background: linear-gradient(120deg, var(--paper) 0%, #fafafa 40%, var(--paper-shade) 100%);
  }
  .banner-art {
    position: absolute;
    inset: 0;
    width: 1200px;
    height: 300px;
  }
  .city-label {
    position: absolute;
    background: var(--accent-orange);
    color: var(--white);
    display: flex;
    align-items: center;
    justify-content: center;
  }
  .city-label--zurich {
    left: 57px;
    top: 40px;
    width: 147px;
    height: 43px;
    font-family: "Noto Serif", serif;
    font-weight: 700;
    font-size: 28px;
  }
  .city-label--hongkong {
    left: 995px;
    top: 158px;
    width: 147px;
    height: 43px;
    font-family: "Noto Sans TC", sans-serif;
    font-weight: 500;
    font-size: 27px;
    letter-spacing: 2px;
  }
  .owner-name {
    position: absolute;
    color: var(--white);
    white-space: nowrap;
  }
  .owner-name--latin {
    left: 56px;
    top: 90px;
    font-family: "Roboto", sans-serif;
    font-weight: 300;
    font-size: 27px;
    line-height: 36px;
  }
  .owner-name--chinese {
    left: 995px;
    top: 205px;
    width: 147px;
    text-align: center;
    font-family: "Noto Sans TC", sans-serif;
    font-weight: 500;
    font-size: 27px;
    line-height: 38px;
    letter-spacing: 1px;
  }
</style>
</head>
<body>
  <section class="banner" aria-label="Profile banner: Zürich and Hong Kong">
    <svg class="banner-art" viewBox="0 0 1200 300" xmlns="http://www.w3.org/2000/svg">
      <defs>
        <radialGradient id="zurich-map-tone" cx="50%" cy="50%" r="50%">
          <stop offset="0%" stop-color="#958a44"/>
          <stop offset="70%" stop-color="#857a36"/>
          <stop offset="100%" stop-color="#857a36" stop-opacity="0"/>
        </radialGradient>
        <radialGradient id="hongkong-map-tone" cx="50%" cy="50%" r="50%">
          <stop offset="0%" stop-color="#4a9cbd"/>
          <stop offset="70%" stop-color="#3e8fb1"/>
          <stop offset="100%" stop-color="#3e8fb1" stop-opacity="0"/>
        </radialGradient>
      </defs>

      <path class="route-arc" d="M200 50 Q 470 -30 780 110" fill="none" stroke="#c9c9c9" stroke-width="1.2" stroke-dasharray="5 5"/>
      <path class="route-arc" d="M430 110 Q 900 -40 1160 120" fill="none" stroke="#d2d2d2" stroke-width="1.2" stroke-dasharray="5 5"/>

      <rect class="band band--zurich" x="0" y="62" width="330" height="83" fill="var(--zurich-blue)"/>
      <rect class="band band--hongkong" x="840" y="182" width="360" height="81" fill="var(--hk-olive)"/>

      <g class="medallion medallion--zurich">
        <circle cx="430" cy="151" r="166" fill="var(--zurich-blue-pale)"/>
        <circle cx="436" cy="151" r="154" fill="var(--zurich-blue)"/>
        <circle cx="430" cy="151" r="134" fill="var(--white)"/>
        <ellipse class="city-map city-map--zurich" cx="425" cy="149" rx="92" ry="114" fill="url(#zurich-map-tone)" role="img" aria-label="Map of the canton of Zürich with district outlines"/>
        <circle cx="403" cy="122" r="6" fill="var(--white)" opacity="0.85"/>
      </g>

      <g class="medallion medallion--hongkong">
        <circle cx="771" cy="152" r="166" fill="var(--hk-olive-pale)"/>
        <circle cx="765" cy="152" r="154" fill="var(--hk-olive)"/>
        <circle cx="771" cy="152" r="134" fill="var(--white)"/>
        <ellipse class="city-map city-map--hongkong" cx="776" cy="149" rx="120" ry="94" fill="url(#hongkong-map-tone)" role="img" aria-label="Map of Hong Kong with district outlines"/>
        <circle cx="778" cy="118" r="6" fill="var(--white)" opacity="0.85"/>
      </g>
    </svg>

    <div class="city-label city-label--zurich">Zürich</div>
    <p class="owner-name owner-name--latin">Tomas Engqvist</p>

    <div class="city-label city-label--hongkong">香港</div>
    <p class="owner-name owner-name--chinese">葉思恆</p>
  </section>
</body>
</html>
```